Stationary project for Velto Mobile Device training company
Stationary project for Velto Mobile Device training company - Electronics
Creative Brief
Use same font as used in my logo
Can use different fonts
Bright & Fun-filled
Dorian Welkett
PO Box 318 Corliss, OR 97342
dorian@brightwake-example.com
www.brightwake-example.com

```html
<!DOCTYPE html>
<html lang="en">
<head>
<meta charset="utf-8">
<title>Brightwake Training Stationery</title>
<link rel="stylesheet" href="https://fonts.googleapis.com/css2?family=Roboto:wght@400;700&family=Roboto+Condensed:wght@700&display=swap">
<style>
  :root {
    --frame: #0e0e0e;
    --board: #a7a7a7;
    --paper: #ffffff;
    --red: #e0141b;
    --red-deep: #7a0a0e;
    --ink: #2a2a2a;
    --ink-soft: #555555;
    --mark: #3a3a3a;
  }
  * { margin: 0; padding: 0; box-sizing: border-box; }
  html, body { width: 1200px; height: 756px; overflow: hidden; background: var(--frame); }
  body { font-family: "Roboto", Arial, sans-serif; color: var(--ink); }

  .board { position: absolute; left: 22px; top: 22px; width: 1156px; height: 712px; background: var(--board); }
  .piece { position: absolute; overflow: hidden; box-shadow: 0 1px 3px rgba(0,0,0,.35); }
  .swoosh { position: absolute; left: 0; bottom: 0; width: 100%; display: block; }
  address { font-style: normal; }

  .brand { display: flex; align-items: center; gap: 8px; }
  .brand-dot { border-radius: 50%; background: var(--mark); flex: none; }
  .brand-name { font-family: "Roboto Condensed", Arial, sans-serif; font-weight: 700; color: var(--ink); white-space: nowrap; letter-spacing: .5px; }
  .tagline { font-size: 8px; color: var(--ink-soft); letter-spacing: 1px; }

  /* letterhead */
  .letterhead { left: 69px; top: 43px; width: 485px; height: 631px; background: var(--paper); }
  .letterhead .brand { position: absolute; left: 22px; top: 24px; }
  .letterhead .brand-dot { width: 44px; height: 44px; }
  .letterhead .brand-name { font-size: 20px; }
  .letterhead .tagline { margin-top: 2px; }
  .letterhead .contact { position: absolute; left: 14px; bottom: 16px; font-size: 8.5px; line-height: 12px; color: #fff; }

  /* business card front */
  .card-front { left: 566px; top: 43px; width: 211px; height: 115px; background: var(--paper); }
  .card-front .brand { position: absolute; left: 10px; top: 9px; gap: 5px; }
  .card-front .brand-dot { width: 22px; height: 22px; }
  .card-front .brand-name { font-size: 10px; }
  .card-front .tagline { font-size: 5px; letter-spacing: .5px; }
  .card-front .person { position: absolute; left: 0; width: 100%; top: 38px; text-align: center; font-size: 7.5px; color: var(--red); font-weight: 700; }
  .card-front .contact { position: absolute; left: 10px; top: 52px; font-size: 5px; line-height: 6.5px; color: var(--ink-soft); }

  .card-simple { display: flex; align-items: center; justify-content: center; }
  .card-simple .brand-dot { width: 40px; height: 40px; }
  .card-simple .brand-name { font-size: 10px; }
  .card-white { left: 873px; top: 88px; width: 197px; height: 118px; background: var(--paper); border-radius: 6px; }
  .card-red { left: 657px; top: 180px; width: 199px; height: 117px; border-radius: 6px; background: radial-gradient(circle at 55% 45%, #e8262c, #9c0c11 80%); }
  .card-red .brand-name { color: #fff; }
  .card-red .brand-dot { background: #2a2a2a; }
  .card-black { left: 873px; top: 242px; width: 219px; height: 118px; border-radius: 6px; background: radial-gradient(circle at 50% 50%, #4a4a4a, #050505 70%); }
  .card-black .brand-name { color: #fff; }
  .card-black .brand-dot { background: #8a8a8a; }

  /* envelope */
  .envelope { left: 566px; top: 357px; width: 526px; height: 317px; background: var(--paper); border-radius: 4px; }
  .envelope .flap { position: absolute; left: 0; top: 0; width: 100%; display: block; }
  .envelope .flap-mark { position: absolute; left: 242px; top: 36px; width: 42px; height: 42px; border-radius: 50%; background: var(--mark); border: 3px solid #fff; }
  .envelope .brand { position: absolute; left: 14px; top: 128px; gap: 10px; }
  .envelope .brand-dot { width: 54px; height: 54px; }
  .envelope .brand-name { font-size: 24px; }
  .envelope .address { position: absolute; left: 14px; top: 290px; font-size: 9px; color: var(--ink); }
</style>
</head>
<body>
<main class="board">

  <section class="piece letterhead">
    <div class="brand">
      <span class="brand-dot"></span>
      <div>
        <div class="brand-name">Brightwake Training</div>
        <div class="tagline">mobile training on the go</div>
      </div>
    </div>
    <svg class="swoosh" viewBox="0 0 485 120" height="120" preserveAspectRatio="none" aria-hidden="true">
      <defs>
        <linearGradient id="lh-red" x1="0" x2="1" y1="0" y2="0">
          <stop offset="0" stop-color="#e0141b"/>
          <stop offset=".6" stop-color="#c11017"/>
          <stop offset="1" stop-color="#7a0a0e"/>
        </linearGradient>
      </defs>
      <path d="M0 18 Q240 0 485 26 L485 120 L0 120 Z" fill="#111"/>
      <path d="M0 26 Q250 8 485 34 L485 120 L0 120 Z" fill="url(#lh-red)"/>
    </svg>
    <address class="contact">
      PO Box 318 Corliss, OR 97342<br>
      Phone: 541.555.0143<br>
      dorian@brightwake-example.com<br>
      www.brightwake-example.com
    </address>
  </section>

  <section class="piece card-front">
    <div class="brand">
      <span class="brand-dot"></span>
      <div>
        <div class="brand-name">Brightwake Training</div>
        <div class="tagline">mobile training on the go</div>
      </div>
    </div>
    <div class="person">Dorian Welkett</div>
    <address class="contact">
      PO Box 318 Corliss, OR 97342<br>
      Phone: 541.555.0143<br>
      dorian@brightwake-example.com<br>
      www.brightwake-example.com
    </address>
    <svg class="swoosh" viewBox="0 0 211 34" height="34" preserveAspectRatio="none" aria-hidden="true">
      <defs>
        <linearGradient id="bc-red" x1="0" x2="1">
          <stop offset="0" stop-color="#e0141b"/>
          <stop offset="1" stop-color="#7a0a0e"/>
        </linearGradient>
      </defs>
      <path d="M0 6 Q100 0 211 8 L211 34 L0 34 Z" fill="#111"/>
      <path d="M0 10 Q105 3 211 12 L211 34 L0 34 Z" fill="url(#bc-red)"/>
    </svg>
  </section>

  <section class="piece card-simple card-white">
    <div class="brand"><span class="brand-dot"></span><span class="brand-name">Brightwake Training</span></div>
  </section>

  <section class="piece card-simple card-red">
    <div class="brand"><span class="brand-dot"></span><span class="brand-name">Brightwake Training</span></div>
  </section>

  <section class="piece card-simple card-black">
    <div class="brand"><span class="brand-dot"></span><span class="brand-name">Brightwake Training</span></div>
  </section>

  <section class="piece envelope">
    <svg class="flap" viewBox="0 0 526 80" height="80" preserveAspectRatio="none" aria-hidden="true">
      <defs>
        <linearGradient id="env-flap" x1="0" x2="1">
          <stop offset="0" stop-color="#7a0a0e"/>
          <stop offset=".5" stop-color="#e0141b"/>
          <stop offset="1" stop-color="#7a0a0e"/>
        </linearGradient>
      </defs>
      <path d="M0 0 L526 0 L526 52 Q263 84 0 52 Z" fill="url(#env-flap)"/>
    </svg>
    <span class="flap-mark"></span>
    <div class="brand">
      <span class="brand-dot"></span>
      <div>
        <div class="brand-name">Brightwake Training</div>
        <div class="tagline">mobile training on the go</div>
      </div>
    </div>
    <address class="address">PO Box 318 Corliss, OR 97342</address>
    <svg class="swoosh" viewBox="0 0 526 50" height="50" preserveAspectRatio="none" aria-hidden="true">
      <defs>
        <linearGradient id="env-red" x1="0" x2="1">
          <stop offset="0" stop-color="#e0141b"/>
          <stop offset="1" stop-color="#7a0a0e"/>
        </linearGradient>
      </defs>
      <path d="M200 50 Q380 6 526 4 L526 50 Z" fill="#111"/>
      <path d="M230 50 Q400 14 526 12 L526 50 Z" fill="url(#env-red)"/>
    </svg>
  </section>

</main>
</body>
</html>
```